Bold Website Design for Fitness Trainer - No Coding

We are in need of a bold and unique website design for a personal fitness training company, www.TessaLorvel.com. We need DESIGN ONLY for three pages. These will be a homepage, a lead capture page, and one internal page with a sidebar. The design will be used for coding a wordpress theme, if that matters for the designer.

Tessa Lorvel Fitness Training
2738 E 19th St #415
Austin, TX 78705
512-607-4918
http://www.tessalorvel.com

Target Market(s)

18-45 year old male and females making 80k+ a year and looking to get stronger and in shape.

Industry/Entity Type

Fitness

Number of Pages Required

3 page

Font styles to use
Sans Serif

Requirements
Must have
• See attached design specs file.
Nice to have
Should not have
• Boxed layout.
• Dark Background.

```html
<!DOCTYPE html>
<html lang="en">
<head>
<meta charset="utf-8">
<title>Tessa Lorvel Fitness Training</title>
<link href="https://fonts.googleapis.com/css2?family=Montserrat:wght@400;600;700&family=Open+Sans:ital,wght@0,400;0,600;0,700;1,400&display=swap" rel="stylesheet">
<style>
:root{
  --pink:#e5127e;
  --blue:#1ea2e6;
  --blue-dark:#1890cf;
  --ink:#222;
  --text:#555;
  --muted:#888;
  --light:#f3f3f3;
  --panel:#f3eeee;
  --footer:#eceff1;
  --white:#fff;
}
*{margin:0;padding:0;box-sizing:border-box}
html,body{width:1200px;height:3854px;overflow:hidden}
body{font-family:"Open Sans",Arial,sans-serif;color:var(--text);background:var(--white);font-size:13px;line-height:1.6;position:relative}
h1,h2,h3,h4{font-family:"Montserrat",Arial,sans-serif;color:var(--ink)}
.wrap{width:1004px;margin:0 auto;position:relative}
.photo{display:block}

/* top bar */
.topbar{height:34px;border-bottom:1px solid #e4e4e4}
.topbar .wrap{display:flex;align-items:center;height:34px;font-size:11px;color:#444}
.topbar .info{display:flex;align-items:center;gap:6px;margin-right:22px}
.topbar .social{margin-left:auto;display:flex;gap:6px}
.topbar .social span{width:20px;height:20px;border:1px solid #555;border-radius:50%}

/* header */
.header{height:164px;display:flex;align-items:center;justify-content:center}
.brand{display:flex;align-items:center;gap:14px}
.brand .mark{width:92px;height:92px;border-radius:50%;background:var(--pink)}
.brand .name{font-family:"Montserrat",Arial,sans-serif;font-weight:700;font-size:34px;color:var(--ink);line-height:1.1}

/* nav */
.nav{height:52px;background:var(--blue)}
.nav ul{list-style:none;display:flex;height:52px}
.nav li{width:146px;text-align:center;line-height:52px;color:var(--white);font-family:"Montserrat",Arial,sans-serif;font-size:13px;font-weight:600;margin-right:4px}
.nav li.active{background:var(--pink)}

/* hero */
.hero{height:513px;position:relative;background:linear-gradient(120deg,#5a5a5a,#9a9a9a 45%,#6e6e6e);}
.hero .photo{position:absolute;inset:0}
.hero h1{position:absolute;top:200px;width:100%;text-align:center;color:var(--white);font-size:32px;letter-spacing:2px;font-weight:600}
.hero .arrow{position:absolute;top:210px}
.signup{position:absolute;left:0;right:0;bottom:0;height:154px;background:rgba(20,20,20,.72)}
.signup h2{color:var(--white);font-size:20px;padding-top:42px;letter-spacing:.5px}
.signup form{display:flex;gap:24px;margin-top:12px}
.signup .field{width:240px;height:40px;background:var(--white);font-size:11px;color:#777;padding:0 10px;line-height:40px}
.signup .btn{width:154px;height:40px;background:var(--pink);color:var(--white);font-size:11px;font-weight:700;text-align:center;line-height:40px}

/* services */
.services{height:578px;padding-top:52px;text-align:center}
.section-title{font-size:27px;font-weight:700;letter-spacing:.5px}
.intro{width:680px;margin:20px auto 0;font-size:12px;line-height:20px}
.cards{display:flex;justify-content:space-between;margin-top:40px;text-align:left}
.card{width:320px;height:340px;background:var(--white);box-shadow:0 4px 10px rgba(0,0,0,.14)}
.card .photo{height:205px}
.card h3{font-size:15px;font-weight:600;margin:18px 20px 6px}
.card p{font-size:11px;line-height:18px;margin:0 20px}

/* testimonials */
.testimonials{height:406px;position:relative;background:linear-gradient(100deg,#3a3a3a,#6b6b6b 55%,#4a4a4a)}
.testimonials .photo{position:absolute;inset:0}
.testimonials h2{position:absolute;top:78px;left:0;right:0;text-align:center;color:var(--white);font-size:27px}
.avatar{position:absolute;left:160px;top:147px;width:188px;height:188px;border-radius:50%;border:5px solid var(--pink);background:linear-gradient(#8c7a70,#5e4f48)}
.quote{position:absolute;left:450px;top:182px;width:560px;color:#eee;font-style:italic;font-size:13px;line-height:23px}
.quote .mark{position:absolute;left:-36px;top:-8px;font-size:50px;color:#ccc;font-family:Georgia,serif}
.quote .who{position:absolute;left:0;top:104px;font-style:normal;color:var(--pink);font-weight:700;font-size:12px}
.quote .role{position:absolute;left:0;top:124px;font-style:normal;font-size:11px;color:#ddd}
.dots{position:absolute;left:1012px;top:302px;display:flex;gap:5px}
.dots span{width:10px;height:10px;border-radius:50%;background:#bbb}

/* feeds */
.feeds{height:437px;padding-top:52px}
.feeds .wrap{display:flex;justify-content:space-between}
.feed h2{font-size:26px;margin-bottom:18px}
.insta{width:480px}
.fb{width:491px;position:relative}
.feed .box{height:311px;background:var(--panel)}
.insta .grid{display:grid;grid-template-columns:repeat(7,56px);gap:10px;padding:14px 0 0 36px}
.insta .grid span{height:56px}
.insta .foot,.fb .foot{border-top:1px solid #ddd;margin-top:18px;height:60px;display:flex;align-items:center;padding-left:36px;gap:10px;font-size:12px;color:#333}
.fb .foot{margin-top:0;padding-left:24px}
.insta .foot .sq,.fb .foot .sq{width:22px;height:22px;background:#333;border-radius:4px}
.fb .foot .sq{background:#3b5998;width:18px;height:18px;border-radius:2px}
.fb .nav-arrows{position:absolute;right:4px;top:10px;color:#999;font-size:16px}
.post{display:flex;padding:24px 24px 0;height:125px}
.post .thumb{width:100px;height:72px;flex:none;margin-top:4px}
.post .txt{margin-left:12px;font-size:11px;line-height:16px}
.post .txt b{color:#1a3f8f;font-weight:600}
.post .meta{margin-top:6px;font-weight:600;color:#333;display:flex;align-items:center;gap:6px}

/* blog */
.blog{height:1041px;background:var(--light);padding-top:72px}
.blog h2{font-size:26px;margin-left:16px;margin-bottom:54px}
.entry{background:var(--white);height:257px;margin-bottom:28px;display:flex;padding:32px 24px}
.entry .thumb{width:284px;height:196px;flex:none;border:1px solid #ddd;padding:4px;background:var(--white)}
.entry .thumb .photo{height:100%}
.entry .body{margin-left:20px;flex:1}
.entry h3{font-size:24px;font-weight:600;line-height:30px}
.entry .date{display:flex;align-items:center;gap:8px;font-size:11px;margin:12px 0 10px;color:#444}
.entry p{font-size:11px;line-height:20px}
.entry .more{color:var(--pink);font-size:11px;font-weight:600;margin-top:14px;display:block}

/* cta */
.cta{height:303px;text-align:center;padding-top:62px}
.cta h2{font-size:26px}
.cta p{width:900px;margin:14px auto 0;font-size:12px;line-height:21px}
.cta .btn{display:inline-block;margin-top:22px;width:152px;height:44px;line-height:44px;background:var(--pink);color:var(--white);font-size:11px;font-weight:700}

/* footer */
.footer{height:265px;background:var(--footer);padding-top:50px}
.footer .wrap{display:flex}
.col h4{font-size:18px;margin-bottom:16px;letter-spacing:.5px}
.col{font-size:11px;line-height:20px;color:#444}
.col.about{width:267px;padding-right:50px}
.col.links{width:213px}
.col.contact{width:275px}
.col.news{width:249px}
.col ul{list-style:none}
.col ul li{line-height:22px}
.col .line{display:flex;align-items:center;gap:8px;margin-top:4px}
.col .input{height:28px;background:var(--white);margin-top:10px;line-height:28px;padding-left:10px;color:#999}
.col .btn{display:inline-block;margin-top:12px;background:var(--pink);color:var(--white);padding:0 18px;line-height:30px;font-weight:600}
.bottombar{height:61px;background:var(--blue);color:var(--white);font-size:11px;line-height:61px;text-align:center;position:relative}
.bottombar .top{position:absolute;right:40px;top:0}
</style>
</head>
<body>

<div class="topbar">
  <div class="wrap">
    <div class="info">
      <svg width="10" height="12" viewBox="0 0 10 12"><path d="M2 0h3l1 3-2 1a7 7 0 0 0 3 4l1-2 3 1v3c0 1-1 2-2 2C5 12 0 7 0 2 0 1 1 0 2 0z" fill="#1ea2e6"/></svg>
      <span>(1) 700 555-0142</span>
    </div>
    <div class="info">
      <svg width="10" height="13" viewBox="0 0 10 13"><path d="M5 0a5 5 0 0 1 5 5c0 3-5 8-5 8S0 8 0 5a5 5 0 0 1 5-5z" fill="#1ea2e6"/><circle cx="5" cy="5" r="2" fill="#fff"/></svg>
      <span>Lorem Ipsum is simply dummy text</span>
    </div>
    <div class="social"><span></span><span></span><span></span><span></span><span></span></div>
  </div>
</div>

<header class="header">
  <div class="brand">
    <span class="mark"></span>
    <span class="name">Tessa Lorvel<br>Fitness Training</span>
  </div>
</header>

<nav class="nav">
  <ul class="wrap">
    <li class="active">HOME</li><li>PROGRAMS</li><li>MEET YOUR TRAINER</li><li>BLOG</li><li>CONTACT ME</li><li>FREE SESSION!</li>
  </ul>
</nav>

<section class="hero">
  <div class="photo" role="img" aria-label="Black and white photo of a group fitness class exercising"></div>
  <svg class="arrow" style="left:48px" width="14" height="26" viewBox="0 0 14 26"><path d="M12 2 2 13l10 11" stroke="#ddd" stroke-width="2" fill="none"/></svg>
  <svg class="arrow" style="right:48px" width="14" height="26" viewBox="0 0 14 26"><path d="M2 2l10 11L2 24" stroke="#ddd" stroke-width="2" fill="none"/></svg>
  <h1>FITNESS TRANNING</h1>
  <div class="signup">
    <div class="wrap">
      <h2>GET STARTED TODAY - YOUR FIRST SESSIONS IS FREE!</h2>
      <form>
        <div class="field">Username</div>
        <div class="field">New Password</div>
        <div class="field">New Password Confirm</div>
        <div class="btn">SUBMIT</div>
      </form>
    </div>
  </div>
</section>

<section class="services">
  <div class="wrap">
    <h2 class="section-title">OUR SERVICES</h2>
    <p class="intro">Lorem Ipsum is simply dummy text of the printing and typesetting industry. Lorem Ipsum has been the industry's standard dummy text ever since the 1500s, when an unknown printer took a galley of type and scrambled it to make a type specimen book.</p>
    <div class="cards">
      <article class="card">
        <div class="photo" role="img" aria-label="Woman stretching on a gym floor" style="background:linear-gradient(135deg,#d9cfc4,#b9a79a 50%,#e7e1da)"></div>
        <h3>BONORUM ET MALORUM</h3>
        <p>Sed ut perspiciatis unde omnis iste natus error sit voluptatem accusantium doloremque laudantium, totam rem aperiam, eaque ipsa quae ab illo invent veritatis .</p>
      </article>
      <article class="card">
        <div class="photo" role="img" aria-label="Group stretching class in a bright studio" style="background:linear-gradient(135deg,#8fb4d0,#c8d6e2 50%,#6f90ad)"></div>
        <h3>FINIBUS BONORUM ET MALORUM</h3>
        <p>Sed ut perspiciatis unde omnis iste natus error sit voluptatem accusantium doloremque laudantium, totam rem aperiam, eaque ipsa quae ab illo invent veritatis .</p>
      </article>
      <article class="card">
        <div class="photo" role="img" aria-label="Women doing an aerobics workout" style="background:linear-gradient(135deg,#c7c4c9,#9d95a3 50%,#dcd8dd)"></div>
        <h3>DENOUNCE WITH RIGHTEOUS</h3>
        <p>Sed ut perspiciatis unde omnis iste natus error sit voluptatem accusantium doloremque laudantium, totam rem aperiam, eaque ipsa quae ab illo invent veritatis .</p>
      </article>
    </div>
  </div>
</section>

<section class="testimonials">
  <div class="photo" role="img" aria-label="Dark gym background with a woman training"></div>
  <h2>TESTIMONIALS</h2>
  <div class="avatar" role="img" aria-label="Portrait of a client"></div>
  <div class="quote">
    <span class="mark">“</span>
    Lorem Ipsum is simply dummy text of the printing and typesetting industry. Lorem Ipsum has been the industry's standard dummy text ever since the 1500s, when an unknown printer took a galley of type and scrambled it to make a type specimen book....
    <span class="who">JANA WRELLBY</span>
    <span class="role">Fitness Enthusiast</span>
  </div>
  <div class="dots"><span></span><span></span></div>
</section>

<section class="feeds">
  <div class="wrap">
    <div class="feed insta">
      <h2>SNAPGRAM FEED FEED</h2>
      <div class="box">
        <div class="grid">
          <span class="photo" role="img" aria-label="Feed photo" style="background:#5a4a52"></span>
          <span class="photo" role="img" aria-label="Feed photo" style="background:#8a6a5a"></span>
          <span class="photo" role="img" aria-label="Feed photo" style="background:#4f6a55"></span>
          <span class="photo" role="img" aria-label="Feed photo" style="background:#9a4a3a"></span>
          <span class="photo" role="img" aria-label="Feed photo" style="background:#3f3050"></span>
          <span class="photo" role="img" aria-label="Feed photo" style="background:#6a5060"></span>
          <span class="photo" role="img" aria-label="Feed photo" style="background:#705040"></span>
          <span class="photo" role="img" aria-label="Feed photo" style="background:#5d7a4a"></span>
          <span class="photo" role="img" aria-label="Feed photo" style="background:#b03040"></span>
          <span class="photo" role="img" aria-label="Feed photo" style="background:#7a6a50"></span>
          <span class="photo" role="img" aria-label="Feed photo" style="background:#4a5a6a"></span>
          <span class="photo" role="img" aria-label="Feed photo" style="background:#8a3a50"></span>
          <span class="photo" role="img" aria-label="Feed photo" style="background:#a07040"></span>
          <span class="photo" role="img" aria-label="Feed photo" style="background:#6a7a8a"></span>
          <span class="photo" role="img" aria-label="Feed photo" style="background:#7a5a40"></span>
          <span class="photo" role="img" aria-label="Feed photo" style="background:#b0a080"></span>
          <span class="photo" role="img" aria-label="Feed photo" style="background:#5a4040"></span>
          <span class="photo" role="img" aria-label="Feed photo" style="background:#a05070"></span>
          <span class="photo" role="img" aria-label="Feed photo" style="background:#3a5a7a"></span>
          <span class="photo" role="img" aria-label="Feed photo" style="background:#6a8aa0"></span>
          <span class="photo" role="img" aria-label="Feed photo" style="background:#8a5060"></span>
        </div>
        <div class="foot"><span class="sq"></span>Snapgram</div>
      </div>
    </div>
    <div class="feed fb">
      <h2>FACEPAGE FEED</h2>
      <span class="nav-arrows">‹ ›</span>
      <div class="box">
        <div class="post">
          <div class="thumb photo" role="img" aria-label="Trainer photo" style="background:linear-gradient(135deg,#e8e0d8,#b8a898)"></div>
          <div class="txt"><b>Voluptatem accusantium doloremque lauda ntium, totam rem aperiam, eaque ipsa</b> quae abi aspernatur aut odit aut fugit, sed quia consequuntur magni dolores eos qui ratione
            <div class="meta"><svg width="12" height="10" viewBox="0 0 12 10"><path d="M0 4l5-4v2c4 0 7 2 7 8-1-3-3-4-7-4v2z" fill="#333"/></svg>909 Shares/ may 29,2015</div></div>
        </div>
        <div class="post">
          <div class="thumb photo" role="img" aria-label="Group class photo" style="background:linear-gradient(135deg,#d8c8c8,#a88890)"></div>
          <div class="txt"><b>Voluptatem accusantium doloremque lauda ntium, totam rem aperiam, eaque ipsa</b> quae abi aspernatur aut odit aut fugit, sed quia consequuntur magni dolores eos qui ratione
            <div class="meta"><svg width="12" height="10" viewBox="0 0 12 10"><path d="M0 4l5-4v2c4 0 7 2 7 8-1-3-3-4-7-4v2z" fill="#333"/></svg>909 Shares/ may 29,2015</div></div>
        </div>
        <div class="foot"><span class="sq"></span>Facepage sociak plugin</div>
      </div>
    </div>
  </div>
</section>

<section class="blog">
  <div class="wrap">
    <h2>OUR BLOG</h2>
    <article class="entry">
      <div class="thumb"><div class="photo" role="img" aria-label="Group doing a stretching class" style="background:linear-gradient(135deg,#b8c8d8,#7890a8 50%,#d0d8e0)"></div></div>
      <div class="body">
        <h3>Muscular Strength Fitness</h3>
        <div class="date"><svg width="12" height="12" viewBox="0 0 12 12"><rect x="0" y="2" width="12" height="10" fill="#444"/><rect x="1" y="5" width="10" height="6" fill="#fff"/></svg>February 14,2015</div>
        <p>Sed ut perspiciatis unde omnis iste natus error sit voluptatem accusantium doloremque laudantium, totam rem aperiam, eaque ipsa quae ab illo inventore veritatis et quasi architecto beatae vitae dicta sunt explicabo. Nemo enim ipsam voluptatem quia voluptas sit aspernatur aut odit aut fugit, sed quia consequuntur magni dolores eos qui ratione voluptatem sequi nesciunt. Neque porro quisquam est</p>
        <span class="more">READ MORE &gt;&gt;</span>
      </div>
    </article>
    <article class="entry">
      <div class="thumb"><div class="photo" role="img" aria-label="Women exercising on step platforms" style="background:linear-gradient(135deg,#e0e0e0,#a8a8a8 50%,#d8d8d8)"></div></div>
      <div class="body">
        <h3>Women Strength Training</h3>
        <div class="date"><svg width="12" height="12" viewBox="0 0 12 12"><rect x="0" y="2" width="12" height="10" fill="#444"/><rect x="1" y="5" width="10" height="6" fill="#fff"/></svg>February 14,2015</div>
        <p>Sed ut perspiciatis unde omnis iste natus error sit voluptatem accusantium doloremque laudantium, totam rem aperiam, eaque ipsa quae ab illo inventore veritatis et quasi architecto beatae vitae dicta sunt explicabo. Nemo enim ipsam voluptatem quia voluptas sit aspernatur aut odit aut fugit, sed quia consequuntur magni dolores eos qui ratione voluptatem sequi nesciunt. Neque porro quisquam est</p>
        <span class="more">READ MORE &gt;&gt;</span>
      </div>
    </article>
    <article class="entry">
      <div class="thumb"><div class="photo" role="img" aria-label="Indoor cycling class" style="background:linear-gradient(135deg,#c8a0a0,#805860 50%,#b89090)"></div></div>
      <div class="body">
        <h3>The do’s and don’ts of &nbsp;fitness</h3>
        <div class="date"><svg width="12" height="12" viewBox="0 0 12 12"><rect x="0" y="2" width="12" height="10" fill="#444"/><rect x="1" y="5" width="10" height="6" fill="#fff"/></svg>February 14,2015</div>
        <p>Sed ut perspiciatis unde omnis iste natus error sit voluptatem accusantium doloremque laudantium, totam rem aperiam, eaque ipsa quae ab illo inventore veritatis et quasi architecto beatae vitae dicta sunt explicabo. Nemo enim ipsam voluptatem quia voluptas sit aspernatur aut odit aut fugit, sed quia consequuntur magni dolores eos qui ratione voluptatem sequi nesciunt. Neque porro quisquam est</p>
        <span class="more">READ MORE &gt;&gt;</span>
      </div>
    </article>
  </div>
</section>

<section class="cta">
  <h2>THE RUNNING FOR FITNESSA</h2>
  <p>Sed ut perspiciatis unde omnis iste natus error sit voluptatem accusantium doloremque laudantium, totam rem aperiam, eaque ipsa quae ab illo inventore veritatis et quasi architecto beatae vitae dicta sunt explicabo. Nemo enim ipsam voluptatem quia voluptas sit aspernatur aut odit aut fugit, sed quia consequuntur magni dolores eos qui ratione voluptatem sequi nesciunt. Neque porro quisquam est, qui dolorem ipsum quia dolor sit amet</p>
  <span class="btn">GET STARTED TODAY</span>
</section>

<footer class="footer">
  <div class="wrap">
    <div class="col about">
      <h4>ABOUT US</h4>
      <p>Lorem Ipsum is simply dummy text of the printing and typesetting industry. Lorem Ipsum has been the industry's standard dummy text ever since the 1500s, when an unknown printer.</p>
    </div>
    <div class="col links">
      <h4>WELCOME</h4>
      <ul><li>Home</li><li>Register Free</li><li>Testimonials</li><li>Hire A Veteran</li><li>About Us</li></ul>
    </div>
    <div class="col contact">
      <h4>CONTACT INFO</h4>
      <p>Tessalorvel<br>120 Street name, City name,<br>Country name, Zip code : 23646222.</p>
      <div class="line"><svg width="10" height="12" viewBox="0 0 10 12"><path d="M2 0h3l1 3-2 1a7 7 0 0 0 3 4l1-2 3 1v3c0 1-1 2-2 2C5 12 0 7 0 2 0 1 1 0 2 0z" fill="#444"/></svg>(233) 555-0187</div>
      <div class="line"><svg width="12" height="10" viewBox="0 0 12 10"><rect width="12" height="10" fill="#444"/><path d="M0 0l6 5 6-5" stroke="#fff" fill="none"/></svg>tessalorvel@fitness.com</div>
    </div>
    <div class="col news">
      <h4>NEWS LETTER</h4>
      <p>Lorem ipsum dolor sit amet, consectetur adipiscing elit.</p>
      <div class="input">Name</div>
      <div class="input">Email Address</div>
      <span class="btn">SUBSCRIBE</span>
    </div>
  </div>
</footer>
<div class="bottombar">© 2015 All Rights Reserved tessalorvel<span class="top">⌃ TOP</span></div>

</body>
</html>
```